Landing page для Vamlor parts
Название сайта (домена, или проекта)
Vamlor parts
Выберите сайты-победители прошлых конкурсов, чтобы дизайнерам был понятен нужный вам стиль
Укажите ссылки на сайты, которые нравятся
https://tridovka.ru/
Оптово-розничные покупатели оригинальных запчастей на автомобили. Средний чек от 30 000 рублей. Мужчины. Мы возим только оригинальные запчасти из Европы, у нас высокая скорость доставки! от 5 рабочих дней.
Этот сайт в принципе нравится https://palmesto.ru/?ysclid=qwert7xz2b814263590 ( не сама цветовая гамма) а расположение блоков.
У нас сайт создан на платформе KRUM. Платформа предполагает использование шаблонных вариантов сайта, то есть сайт реализован на готовом шаблоне. Ниже мы прикладываем используемый шаблон.
https://vamlor-parts.ru/?templateId=31&class=301&color=206351
Важно учитывать, что выход за рамки возможностей шаблона невозможен. Поэтому макет дизайна лендинг-пейджа по техническому заданию, представленному ниже, необходимо разрабатывать строго с учётом функциональных и визуальных возможностей, которые предоставляет данный шаблон сайта.
https://docs.example-files.net/document/d/7Kd_prTq2mXz9WbLe4HnRs0VyUj3cAoF8QgtZ1NxYbPw/edit?tab=t.0
Адаптивность сайта
Десктопная версия, Версия для планшетов, Версия для телефонов

```html
<!DOCTYPE html>
<html lang="ru">
<head>
<meta charset="UTF-8">
<title>Vamlor parts — оригинальные автозапчасти из Европы</title>
<link href="https://fonts.googleapis.com/css2?family=Oswald:wght@400;500&family=Roboto+Condensed:wght@400;500&family=Roboto:wght@400;500&display=swap" rel="stylesheet">
<style>
  :root {
    --header-bg: #1f1f20;
    --hero-bg: #0b0b0c;
    --text-main: #ffffff;
    --text-soft: #d9d9d9;
    --text-muted: #9a9a9a;
    --accent: #8c1518;
    --accent-bright: #b3161c;
    --field-bg: #ffffff;
    --field-text: #a0a0a0;
  }
  * { margin: 0; padding: 0; box-sizing: border-box; }
  html, body { width: 1200px; height: 502px; overflow: hidden; background: var(--hero-bg); }
  body { position: relative; font-family: "Roboto Condensed", sans-serif; color: var(--text-main); }

  .site-header {
    position: absolute; left: 0; top: 0; width: 1200px; height: 83px;
    background: var(--header-bg); z-index: 2;
  }
  .brand {
    position: absolute; left: 108px; top: 28px; display: flex; align-items: center; gap: 8px;
    font-family: "Oswald", sans-serif; font-weight: 500; font-size: 22px; letter-spacing: 1px; color: var(--text-main);
  }
  .brand-dot { width: 12px; height: 12px; border-radius: 50%; background: var(--text-main); }
  .catalog-toggle {
    position: absolute; left: 277px; top: 30px; display: flex; align-items: center; gap: 12px;
    font-family: "Roboto", sans-serif; font-size: 14px; color: var(--text-main);
  }
  .search-field {
    position: absolute; left: 442px; top: 23px; width: 400px; height: 37px;
    background: var(--field-bg); border-radius: 2px;
    display: flex; align-items: center; padding: 0 14px;
    font-family: "Roboto", sans-serif; font-size: 11px; color: var(--field-text);
  }
  .search-field svg { position: absolute; right: 14px; top: 11px; }
  .header-link {
    position: absolute; top: 27px; display: flex; gap: 8px;
    font-family: "Roboto", sans-serif;
  }
  .header-link .label { font-size: 11px; color: var(--text-muted); line-height: 14px; }
  .header-link .value { font-size: 12px; color: var(--text-main); line-height: 16px; }
  .account-link { left: 900px; }
  .cart-link { left: 1030px; }

  .hero { position: absolute; left: 0; top: 83px; width: 1200px; height: 419px;
    background: radial-gradient(ellipse at 70% 40%, #2a2b2e 0%, #131315 45%, var(--hero-bg) 75%); }
  .hero-visual {
    position: absolute; left: 560px; top: 40px; width: 640px; height: 379px;
    background:
      radial-gradient(ellipse 60% 45% at 62% 58%, #3a3e44 0%, #1c1e21 55%, rgba(11,11,12,0) 100%),
      radial-gradient(ellipse 80% 30% at 50% 95%, #1d1e20 0%, rgba(11,11,12,0) 100%);
  }
  .hero-title {
    position: absolute; left: 108px; top: 80px;
    font-family: "Oswald", sans-serif; font-weight: 500; font-size: 36px; letter-spacing: 0.5px;
    text-transform: uppercase; color: var(--text-main);
  }
  .hero-subtitle {
    position: absolute; left: 108px; top: 132px;
    font-family: "Oswald", sans-serif; font-weight: 400; font-size: 20px; letter-spacing: 0.5px;
    text-transform: uppercase; color: var(--text-soft);
  }
  .hero-benefits {
    position: absolute; left: 108px; top: 234px;
    font-family: "Roboto Condensed", sans-serif; font-size: 17px; text-transform: uppercase; color: var(--text-soft);
  }
  .hero-actions { position: absolute; left: 108px; top: 285px; display: flex; gap: 10px; }
  .btn {
    width: 254px; height: 40px; display: flex; align-items: center; justify-content: center;
    font-family: "Roboto Condensed", sans-serif; font-weight: 500; font-size: 16px; text-transform: uppercase;
    color: var(--text-main); border-radius: 2px;
  }
  .btn-primary { background: var(--accent); }
  .btn-outline { background: rgba(10,10,11,0.6); border: 1.5px solid var(--accent-bright); }
</style>
</head>
<body>
  <header class="site-header">
    <div class="brand"><span class="brand-dot"></span>VAMLOR</div>
    <div class="catalog-toggle">
      <svg width="18" height="14" viewBox="0 0 18 14"><g fill="#fff"><rect y="0" width="18" height="2"/><rect y="6" width="18" height="2"/><rect y="12" width="18" height="2"/></g></svg>
      Каталоги
    </div>
    <div class="search-field">
      Введите код запчасти или VIN номер автомобиля
      <svg width="14" height="14" viewBox="0 0 14 14"><circle cx="6" cy="6" r="4.5" fill="none" stroke="#9a9a9a" stroke-width="1.5"/><line x1="9.5" y1="9.5" x2="13" y2="13" stroke="#9a9a9a" stroke-width="1.5"/></svg>
    </div>
    <div class="header-link account-link">
      <svg width="16" height="16" viewBox="0 0 16 16"><circle cx="8" cy="5" r="3.5" fill="#8c1518"/><path d="M1 16c0-4 3-6 7-6s7 2 7 6z" fill="#8c1518"/></svg>
      <div><div class="label">Личный кабинет</div><div class="value">Вход</div></div>
    </div>
    <div class="header-link cart-link">
      <svg width="16" height="16" viewBox="0 0 16 16"><path d="M1 2h3l2 9h8l1.5-6H5" fill="none" stroke="#8c1518" stroke-width="1.6"/><circle cx="7" cy="14" r="1.3" fill="#8c1518"/><circle cx="13" cy="14" r="1.3" fill="#8c1518"/></svg>
      <div><div class="label">Корзина</div><div class="value">0 ₽</div></div>
    </div>
  </header>

  <section class="hero">
    <div class="hero-visual" role="img" aria-label="Фотография тёмного седана в дымке на тёмном фоне"></div>
    <h1 class="hero-title">Оригинальные автозапчасти из Европы</h1>
    <p class="hero-subtitle">С доставкой от 3 рабочих дней</p>
    <p class="hero-benefits">100% оригинал • гарантия совместимости • без посредников</p>
    <div class="hero-actions">
      <div class="btn btn-primary">Подобрать запчасти</div>
      <div class="btn btn-outline">Получить консультацию</div>
    </div>
  </section>
</body>
</html>
```